Website for an AdOps/Media Agency

We need a logo for an ad operations firm. We help websites to maximize their advertising revenues by optimizing their ad networks, configurations, technologies, etc. The name is Zornival, or ZorNival, to communicate that we take them to the top of their revenue potential. We want to also communicate, trust us to handle your adops, we take care of the hassle (it's an industry in continual technological innovation -- hard to stay on top of, and heavily manual, reporting, etc) and make sure our clients maximize ad revenues. For more info on site ideas/desires: https://files.brelmora.com/doc/7QxTbn2Lw9Rk4Vz8Hc3Md6Fp1Ys5Ga0Je/view?usp=sharing
Updates

Project Deadline Extended Reason: Apologies, I got caught up in other things. This is now priority, and will be guaranteed. I will also include an extra coding fee for a WP site and increase the budget. Thanks for your understanding! Added Thursday, July 7, 2016

Target Market(s)

Ad Operations/Media Consultancy

Industry/Entity Type

Ad Agency

Number of Pages Required

1 page

Font styles to use
Sans Serif

Requirements
Must have
• I like clean and simple, nice images, scrolling down.
Nice to have
• I like clean, fresh white running through the site. Note, I listed us as an ad agency, but only because there was no adops. We work with ad agencies, but we are more agents for publishers.
Should not have
• To much clutter.

```html
<!DOCTYPE html>
<html lang="en">
<head>
<meta charset="utf-8">
<title>Zornival — Publisher Partnership</title>
<link rel="stylesheet" href="https://fonts.googleapis.com/css2?family=Questrial&family=Arimo:wght@400;700&display=swap">
<style>
  :root {
    --white: #ffffff;
    --ink: #2a2a2a;
    --nav-ink: #333333;
    --accent: #ff8a00;
    --logo-square: #2f3438;
    --sky-top: #4f86b8;
    --sky-mid: #a9c2cf;
    --haze: #d9d6c4;
    --rock-light: #d9834a;
    --rock: #c0542a;
    --rock-deep: #8a3218;
    --panel: rgba(40, 52, 62, 0.42);
  }
  * { box-sizing: border-box; margin: 0; padding: 0; }
  html, body { width: 1200px; height: 673px; overflow: hidden; }
  body { font-family: "Questrial", sans-serif; background: var(--white); }

  .page { position: relative; width: 1200px; height: 673px; overflow: hidden; }

  .hero-image {
    position: absolute; inset: 0;
    background:
      radial-gradient(ellipse 45% 35% at 58% 58%, rgba(255,245,225,0.55), transparent 70%),
      linear-gradient(180deg,
        var(--sky-top) 0%,
        var(--sky-mid) 30%,
        var(--haze) 52%,
        var(--rock-light) 72%,
        var(--rock) 86%,
        var(--rock-deep) 100%);
  }

  .site-header {
    position: absolute; top: 0; left: 0; right: 0; height: 80px;
    background: var(--white);
    display: flex; align-items: center;
    box-shadow: 0 2px 6px rgba(0,0,0,0.25);
    z-index: 2;
  }
  .brand { position: absolute; left: 92px; top: 0; height: 80px; display: flex; align-items: center; }
  .brand-square { width: 80px; height: 80px; background: var(--logo-square); }
  .brand-name {
    margin-left: 12px; font-family: "Questrial", sans-serif;
    font-size: 46px; letter-spacing: 6px; color: var(--ink);
  }

  .main-nav { position: absolute; top: 0; left: 528px; height: 80px; }
  .main-nav a {
    position: absolute; top: 30px; white-space: nowrap;
    font-size: 16px; color: var(--nav-ink); text-decoration: none; letter-spacing: 0.3px;
  }
  .main-nav .is-current::after {
    content: ""; position: absolute; left: 0; right: 0; bottom: -9px;
    height: 3px; background: var(--accent);
  }

  .cta-button {
    position: absolute; left: 981px; top: 18px; width: 158px; height: 44px;
    background: var(--accent); color: var(--white); border-radius: 3px;
    font-family: "Arimo", sans-serif; font-size: 17px;
    display: flex; align-items: center; justify-content: center; gap: 10px;
    text-decoration: none;
  }

  .section-title {
    position: absolute; top: 160px; left: 86px; width: 1027px;
    display: flex; align-items: center; justify-content: space-between;
  }
  .section-title .rule { width: 268px; height: 2px; background: var(--white); }
  .section-title h1 {
    font-family: "Arimo", sans-serif; font-weight: 700; font-size: 33px;
    color: var(--white); letter-spacing: 0.8px;
  }

  .intro-panel {
    position: absolute; left: 86px; top: 260px; width: 1031px; height: 310px;
    background: var(--panel); border-radius: 4px;
    padding: 44px 60px 0; text-align: center;
    color: var(--white); font-size: 15.4px; line-height: 31.6px; letter-spacing: 0.6px;
  }
  .intro-panel p + p { margin-top: 44px; }
</style>
</head>
<body>
<div class="page">
  <div class="hero-image" role="img" aria-label="Photograph of a hiker with raised arms standing on red sandstone rocks under a bright blue sky"></div>

  <header class="site-header">
    <div class="brand">
      <span class="brand-square"></span>
      <span class="brand-name">ZORNIVAL</span>
    </div>
    <nav class="main-nav">
      <a href="#" style="left:0">HOME</a>
      <a href="#" class="is-current" style="left:93px">ABOUT</a>
      <a href="#" style="left:189px">SERVICES</a>
      <a href="#" style="left:303px">CONTACT US</a>
    </nav>
    <a href="#" class="cta-button">Free Consult <span>&#x276F;</span></a>
  </header>

  <div class="section-title">
    <span class="rule"></span>
    <h1>PUBLISHER PARTNERSHIP</h1>
    <span class="rule"></span>
  </div>

  <section class="intro-panel">
    <p>Programmatic has revolutionized the advertising playing field. Now, small, medium and large publishers alike all have equal access to the best advertisers and premium cpms.&nbsp; But it’s a fast moving world, and it takes a big team and varied skill set to stay on top of the technologies, players, offers, implementations and optimizations. Our team covers all these skills, and our team wants to be on your team.&nbsp; We work with top publishers helping to maximize their monetization on over 1.5B monthly impressions.</p>
    <p>Let us take over and optimize your adops so you can concentrate on what you do best: your site!</p>
  </section>
</div>
</body>
</html>
```